Crestline Lending Group Business Cards

We are looking to revamp the current business cards each of our locations uses. We are a lending company that specializes in personal loans, title loans, and tax services. We have locations in New Mexico, Texas, and Oklahoma.

We would like a cleaner, sleeker look while still highlighting what we offer. Title Loans, Personal Loans & Tax Services. We also want to include our referral fee somewhere on the card. We would like to see an English option as well as a Spanish option for the cards.

PLEASE NOTE: Some business cards do not include the employee's name but just the store's location, while others will include both.

These are double-sided business cards, and we would like to see proof if possible. I have included proofs of our current business cards for you to review below, as well as our company logo. Feel free to get creative with the logo, etc! Colors should match the logo; however, you do not need to use all of our logo colors if you don't want to.

```html
<!DOCTYPE html>
<html lang="en">
<head>
<meta charset="utf-8">
<title>Crestline Lending Group – Business Cards</title>
<link rel="stylesheet" href="https://fonts.googleapis.com/css2?family=Archivo+Black&family=Arimo:wght@400;700&display=swap">
<style>
  :root {
    --page: #ffffff;
    --paper: #f3f3f3;
    --green-deep: #236b47;
    --green-bright: #207a46;
    --red: #c8313b;
    --white: #ffffff;
  }
  * { margin: 0; padding: 0; box-sizing: border-box; }
  html, body {
    width: 1200px;
    height: 927px;
    overflow: hidden;
    background: var(--page);
  }
  body { position: relative; font-family: "Arimo", Arial, sans-serif; }

  .card {
    position: absolute;
    overflow: hidden;
  }

  /* Front */
  .card--front {
    left: 267px; top: 42px;
    width: 668px; height: 382px;
    background: var(--paper);
  }
  .card__waves {
    position: absolute; left: 0; top: 0;
    width: 668px; height: 382px;
  }
  .brand {
    position: absolute; left: 0; top: 88px; width: 100%;
    text-align: center;
  }
  .brand__name {
    font-family: "Arimo", Arial, sans-serif;
    font-weight: 700;
    font-size: 40px;
    letter-spacing: -0.5px;
    color: var(--green-deep);
    line-height: 1;
  }
  .brand__web {
    margin-top: 12px;
    font-size: 16px;
    color: var(--red);
    padding-left: 150px;
  }
  .contact {
    position: absolute; left: 33px; top: 258px;
    color: var(--white);
    font-family: "Archivo Black", "Arial Black", sans-serif;
    font-style: normal;
  }
  .contact__street, .contact__city { font-size: 18.5px; line-height: 25px; letter-spacing: 0.3px; }
  .contact__phone { font-size: 21px; line-height: 27px; margin-top: 4px; }
  .contact__email { font-family: "Arimo", Arial, sans-serif; font-weight: 700; font-size: 15px; line-height: 17px; }

  .services {
    position: absolute; left: 395px; top: 228px;
    list-style: none;
  }
  .services__item {
    display: flex; align-items: center;
    height: 48.5px;
    color: var(--white);
    font-weight: 700;
    font-size: 26px;
    letter-spacing: 0.3px;
  }
  .services__tick { width: 22px; height: 22px; margin-right: 14px; flex: none; }

  /* Back */
  .card--back {
    left: 277px; top: 526px;
    width: 645px; height: 372px;
    background: var(--green-bright);
  }
  .card__pattern {
    position: absolute; inset: 0;
    background: var(--green-bright);
  }
  .brand--back { top: 166px; }
  .brand--back .brand__name { color: var(--white); font-size: 28px; }
  .brand--back .brand__web { color: var(--white); font-size: 10px; margin-top: 8px; padding-left: 90px; }

  .referral__band {
    position: absolute; left: 0; top: 316px;
    width: 352px; height: 56px;
    background: var(--red);
  }
  .referral__label {
    position: absolute; left: 10px; top: 317px;
    font-family: "Archivo Black", "Arial Black", sans-serif;
    font-size: 41px; line-height: 54px;
    letter-spacing: 1px;
    color: var(--white);
  }
  .referral__upto {
    position: absolute; left: 363px; top: 284px;
    font-size: 34px; line-height: 36px;
    color: var(--white);
  }
  .referral__get {
    position: absolute; left: 364px; top: 325px;
    font-family: "Archivo Black", "Arial Black", sans-serif;
    font-size: 32px; line-height: 36px;
    letter-spacing: 1px;
    color: var(--white);
  }
  .referral__amount {
    position: absolute; left: 464px; top: 284px;
    font-family: "Archivo Black", "Arial Black", sans-serif;
    font-size: 62px; line-height: 76px;
    letter-spacing: -2px;
    color: var(--white);
  }
</style>
</head>
<body>

<section class="card card--front" aria-label="Business card front">
  <svg class="card__waves" viewBox="0 0 668 382" aria-hidden="true">
    <defs>
      <clipPath id="left-half"><rect x="0" y="0" width="334" height="382"/></clipPath>
      <clipPath id="right-half"><rect x="334" y="0" width="334" height="382"/></clipPath>
    </defs>
    <path d="M0,243 Q300,120 668,208 L668,215 Q300,148 0,250 Z" fill="var(--red)"/>
    <path d="M0,256 Q300,162 668,222 L668,382 L0,382 Z" fill="var(--green-deep)" clip-path="url(#left-half)"/>
    <path d="M0,256 Q300,162 668,222 L668,382 L0,382 Z" fill="var(--red)" clip-path="url(#right-half)"/>
  </svg>

  <div class="brand">
    <div class="brand__name">Crestline Lending Group</div>
    <div class="brand__web">www.crestlinelending.com</div>
  </div>

  <address class="contact">
    <div class="contact__street">742 Cedar Avenue</div>
    <div class="contact__city">Rivervale, Texas 75412</div>
    <div class="contact__phone">(505) 555-0147</div>
    <div class="contact__email">hello@crestlinelending.com</div>
  </address>

  <ul class="services">
    <li class="services__item">
      <svg class="services__tick" viewBox="0 0 22 22" aria-hidden="true">
        <circle cx="10" cy="12" r="8" fill="none" stroke="var(--white)" stroke-width="3"/>
        <path d="M5.5,11.5 L9.5,15.5 L20,3" fill="none" stroke="var(--white)" stroke-width="3.2" stroke-linecap="round"/>
      </svg>Title Loans</li>
    <li class="services__item">
      <svg class="services__tick" viewBox="0 0 22 22" aria-hidden="true">
        <circle cx="10" cy="12" r="8" fill="none" stroke="var(--white)" stroke-width="3"/>
        <path d="M5.5,11.5 L9.5,15.5 L20,3" fill="none" stroke="var(--white)" stroke-width="3.2" stroke-linecap="round"/>
      </svg>Personal loans</li>
    <li class="services__item">
      <svg class="services__tick" viewBox="0 0 22 22" aria-hidden="true">
        <circle cx="10" cy="12" r="8" fill="none" stroke="var(--white)" stroke-width="3"/>
        <path d="M5.5,11.5 L9.5,15.5 L20,3" fill="none" stroke="var(--white)" stroke-width="3.2" stroke-linecap="round"/>
      </svg>Tax Services</li>
  </ul>
</section>

<section class="card card--back" aria-label="Business card back">
  <div class="card__pattern" role="img" aria-label="Faint repeating brand pattern on green"></div>

  <div class="brand brand--back">
    <div class="brand__name">Crestline Lending Group</div>
    <div class="brand__web">www.crestlinelending.com</div>
  </div>

  <div class="referral__band"></div>
  <div class="referral__label">Refer a Friend</div>
  <div class="referral__upto">up to</div>
  <div class="referral__get">GET</div>
  <div class="referral__amount">$100</div>
</section>

</body>
</html>
```